Management Company for Associations needs new and improved letterhead

We need a design for letterhead that looks professional. We like designs that can incorporate a lot of space for our letters, a new age professional font, and different styles to choose from. Please use the language in the attached letterhead example. The BPN logo needs to be incorporated in the letterhead; please follow the size requirements for use. We are trying to totally revamp our letterhead.
Industry/Entity Type
Property Management
Font styles to use
Serif
Script
Colors
ec1f27
Requirements
Must have
- BPN Logo in black, K7 logo, Using both Top & Bottom, Red Color used to match logo color.
Nice to have
- (1 design with a watermark using K7 logo)

```html
<!DOCTYPE html>
<html lang="en">
<head>
<meta charset="utf-8">
<title>K7 Letterhead</title>
<link rel="stylesheet" href="https://fonts.googleapis.com/css2?family=Arimo:wght@400;700&display=swap">
<style>
  :root {
    --backdrop: #e9e9ea;
    --paper: #ffffff;
    --ink: #2b2b2b;
    --ink-soft: #555555;
    --brand-red: #ec1f27;
    --band-red: #b8060d;
    --band-grey: #8a8a8c;
    --black: #111111;
  }
  * { box-sizing: border-box; margin: 0; padding: 0; }
  html, body { width: 1200px; height: 1064px; overflow: hidden; }
  body {
    background: var(--backdrop);
    font-family: "Arimo", Arial, sans-serif;
    color: var(--ink);
    position: relative;
  }
  .letterhead {
    position: absolute;
    left: 246px; top: 32px;
    width: 708px; height: 1000px;
    background: var(--paper);
    box-shadow: 0 2px 10px rgba(0,0,0,0.12);
    overflow: hidden;
  }
  .brand {
    position: absolute; left: 56px; top: 46px;
    display: flex; align-items: center; gap: 12px;
  }
  .brand-dot {
    width: 26px; height: 26px; border-radius: 50%;
    background: var(--brand-red);
  }
  .brand-name {
    font-size: 64px; font-weight: 700; color: var(--brand-red);
    line-height: 1;
  }
  .contact {
    position: absolute; right: 56px; top: 58px;
    font-size: 10px; line-height: 1.45; color: var(--ink-soft);
  }
  .contact .label { color: var(--brand-red); }
  .letter {
    position: absolute; left: 56px; top: 170px; width: 440px;
    font-size: 11px; line-height: 1.5;
  }
  .letter .date { margin-bottom: 10px; }
  .letter .salutation { font-weight: 700; }
  .letter .recipient { margin-bottom: 14px; }
  .letter p.body { margin-bottom: 40px; }
  .closing { margin-top: -14px; }
  .signature-mark {
    width: 96px; height: 40px; margin: 10px 0 6px;
    background: linear-gradient(90deg, #d9d9d9, #f2f2f2);
    border-radius: 4px;
  }
  .signer-name { font-weight: 700; }
  .member-mark {
    position: absolute; right: 48px; top: 560px;
    width: 150px; text-align: right; color: var(--black);
    line-height: 1;
  }
  .member-label {
    display: block; font-size: 13px; font-weight: 700;
    letter-spacing: 2px; text-transform: uppercase; margin-bottom: 4px;
  }
  .member-name {
    display: block; font-size: 44px; font-weight: 700;
  }
  .footer-waves { position: absolute; left: 0; top: 0; }
</style>
</head>
<body>
  <main class="letterhead">
    <div class="brand">
      <span class="brand-dot"></span>
      <span class="brand-name">K7</span>
    </div>

    <div class="contact">
      <div><span class="label">Toll Free:</span> 800-555-0142</div>
      <div><span class="label">Email:</span> office@k7manage.com</div>
      <div><span class="label">Web:</span> www.k7manage.com</div>
    </div>

    <section class="letter">
      <div class="date">July 2, 2012</div>
      <div class="salutation">Dear CH,</div>
      <div class="recipient">ABC Building, def St. Country Name</div>
      <p class="body">is simply dummy text of the printing and typesetting industry. Lorem Ipsum has been the industry's standard dummy text ever since the 1500s, when an unknown printer took a galley of type and scrambled it to make a type specimen book. It has survived not only five centuries, but also the leap into electronic typesetting, remaining essentially unchanged. It was popularised in the 1960s with the release of Printwell sheets containing Lorem Ipsum passages, and more recently with desktop publishing software like PageForge Studio including versions of Lorem Ipsum.</p>
      <p class="body">is simply dummy text of the printing and typesetting industry. Lorem Ipsum has been the industry's standard dummy text ever since the 1500s, when an unknown printer took a galley of type and scrambled it to make</p>
      <p class="body">is simply dummy text of the printing and typesetting industry. Lorem Ipsum has been the industry's standard dummy text ever since the 1500s, when an unknown printer took a galley of type and scrambled it to make a type specimen book. It has survived not only five centuries, but also the leap into electronic typesetting, remaining essentially unchanged. It was popularised in the 1960s with the release of Printwell sheets containing Lorem Ipsum passages, and more recently with desktop publishing software like PageForge Studio including versions of Lorem Ipsum.</p>
      <div class="closing">
        <div>Best Regards,</div>
        <div class="signature-mark" role="img" aria-label="Handwritten signature"></div>
        <div class="signer-name">Daniel Reed</div>
        <div>Director</div>
        <div>ABC Building, def St. Country Name</div>
      </div>
    </section>

    <div class="member-mark">
      <span class="member-label">Member of</span>
      <span class="member-name">BPN</span>
    </div>

    <svg class="footer-waves" width="708" height="1000" viewBox="0 0 708 1000" aria-hidden="true">
      <path d="M0 900 C 250 900, 480 815, 708 680 L708 1000 L0 1000 Z" fill="var(--band-grey)"/>
      <path d="M0 914 C 255 914, 485 830, 708 697 L708 1000 L0 1000 Z" fill="var(--paper)"/>
      <path d="M0 922 C 260 922, 490 840, 708 708 L708 1000 L0 1000 Z" fill="var(--band-red)"/>
    </svg>
  </main>
</body>
</html>
```